Migration Lawyers

Company: Dunstan & Co Lawyers & Migration Agents

Name: Graham Dunstan BEc, LLB
Address: Level 18, 72 Hollis Street
Sydney, NSW, Australia 2000

Ph: +61 2 9384 5207
M: 0428316540
E: graham@permitpath-example.org.au
W: www.permitpath-example.org.au

Target Market(s)

Migration Clients

Industry/Entity Type

It Company

Font styles to use
Script

Requirements
Must have
• Logo
Should not have
• Please scale the format to the printing size attached

```html
<!DOCTYPE html>
<html lang="en">
<head>
<meta charset="utf-8">
<title>Dunstan &amp; Co – Business Cards</title>
<link rel="stylesheet" href="https://fonts.googleapis.com/css2?family=Open+Sans:wght@400;600;700&display=swap">
<style>
  :root {
    --backdrop: #6a4125;
    --card-white: #ffffff;
    --card-black: #050505;
    --band-dark: #1a1a1a;
    --band-edge: #8a8a8a;
    --ink: #222222;
    --ink-soft: #3a3a3a;
    --paper-text: #f2f2f2;
  }
  * { margin: 0; padding: 0; box-sizing: border-box; }
  html, body { width: 1200px; height: 850px; overflow: hidden; }
  body {
    background: var(--backdrop);
    font-family: "Open Sans", Arial, sans-serif;
    position: relative;
  }
  .card {
    position: absolute;
    box-shadow: 0 4px 14px rgba(0,0,0,0.35);
    overflow: hidden;
  }
  /* Front card */
  .card-front {
    left: 52px; top: 33px;
    width: 657px; height: 383px;
    background: var(--card-white);
  }
  .front-band {
    position: absolute; left: 0; top: 0;
    width: 657px; height: 90px;
  }
  .holder-name {
    position: absolute; left: 0; right: 0; top: 10px;
    text-align: center;
    color: var(--paper-text);
    font-weight: 700;
    font-size: 21px;
  }
  .holder-name .credentials {
    font-weight: 400;
    font-size: 15px;
    margin-left: 4px;
  }
  .front-brand {
    position: absolute; left: 0; right: 0; top: 148px;
    display: flex; justify-content: center; align-items: center; gap: 14px;
  }
  .brand-circle {
    width: 62px; height: 62px;
    border: 2px solid var(--ink);
    border-radius: 50%;
    flex: none;
  }
  .brand-name {
    font-weight: 700;
    color: var(--ink);
    line-height: 1.15;
  }
  .brand-name .firm { display: block; font-size: 26px; }
  .brand-name .practice { display: block; font-size: 12px; }
  .contact-row {
    position: absolute; left: 0; right: 0;
    display: flex; justify-content: center; align-items: center; gap: 18px;
    font-size: 16px; color: var(--ink-soft);
  }
  .contact-row.phones { top: 299px; }
  .contact-row.web { top: 330px; }
  .contact-item { display: inline-flex; align-items: center; gap: 6px; }
  .contact-item svg { width: 15px; height: 15px; flex: none; }
  .address {
    position: absolute; left: 0; right: 0; top: 374px;
    transform: translateY(-100%);
    padding-bottom: 0;
    text-align: center;
    font-size: 16px; color: var(--ink-soft);
  }
  /* Back card */
  .card-back {
    left: 492px; top: 440px;
    width: 663px; height: 378px;
    background: var(--card-black);
  }
  .back-brand {
    position: absolute; left: 0; right: 0; top: 120px;
    display: flex; justify-content: center; align-items: center; gap: 20px;
  }
  .back-brand .brand-circle {
    width: 110px; height: 110px;
    border: 3px solid var(--paper-text);
  }
  .back-brand .brand-name { color: var(--paper-text); }
  .back-brand .brand-name .firm { font-size: 30px; }
  .back-brand .brand-name .practice { font-size: 13px; }
  .back-web {
    position: absolute; left: 0; right: 0; top: 318px;
    text-align: center;
    color: var(--paper-text);
    font-size: 19px;
  }
</style>
</head>
<body>

  <section class="card card-front" aria-label="Business card front">
    <svg class="front-band" viewBox="0 0 657 90" aria-hidden="true">
      <defs>
        <linearGradient id="bandShade" x1="0" y1="0" x2="0" y2="1">
          <stop offset="0" stop-color="#3a3a3a"/>
          <stop offset="1" stop-color="#0d0d0d"/>
        </linearGradient>
      </defs>
      <path d="M0 0 H657 V34 Q328 78 0 34 Z" fill="url(#bandShade)"/>
      <path d="M0 34 Q328 78 657 34" fill="none" stroke="var(--band-edge)" stroke-width="4"/>
    </svg>
    <div class="holder-name">Graham Dunstan<span class="credentials">BEc, LLB</span></div>

    <div class="front-brand">
      <span class="brand-circle"></span>
      <div class="brand-name">
        <span class="firm">Dunstan &amp; Co</span>
        <span class="practice">Lawyers &amp; Migration Agents</span>
      </div>
    </div>

    <div class="contact-row phones">
      <span class="contact-item">
        <svg viewBox="0 0 16 16" aria-hidden="true"><circle cx="8" cy="8" r="7" fill="none" stroke="#333" stroke-width="1.3"/><path d="M5.5 4.5 l1.5 0 .6 2-1 .8a5 5 0 0 0 2.1 2.1l.8-1 2 .6v1.5c-3.5.3-6.3-2.5-6-6z" fill="#333"/></svg>
        +61 2 9384 5207
      </span>
      <span class="contact-item">
        <svg viewBox="0 0 16 16" aria-hidden="true"><circle cx="8" cy="8" r="7" fill="none" stroke="#333" stroke-width="1.3"/><path d="M5.5 4.5 l1.5 0 .6 2-1 .8a5 5 0 0 0 2.1 2.1l.8-1 2 .6v1.5c-3.5.3-6.3-2.5-6-6z" fill="#333"/></svg>
        0428316540
      </span>
      <span class="contact-item">
        <svg viewBox="0 0 16 16" aria-hidden="true"><rect x="1.5" y="3.5" width="13" height="9" fill="#333"/><path d="M1.5 3.5 L8 9 L14.5 3.5" fill="none" stroke="#fff" stroke-width="1.2"/></svg>
        graham@permitpath-example.org.au
      </span>
    </div>
    <div class="contact-row web">
      <span class="contact-item">
        <svg viewBox="0 0 16 16" aria-hidden="true"><circle cx="8" cy="8" r="6.5" fill="none" stroke="#333" stroke-width="1.3"/><ellipse cx="8" cy="8" rx="3" ry="6.5" fill="none" stroke="#333" stroke-width="1"/><path d="M1.5 8 H14.5" stroke="#333" stroke-width="1"/></svg>
        www.permitpath-example.org.au
      </span>
    </div>
    <div class="address">Level 18, 72 Hollis Street, Australia, Sydney, NSW, 2000</div>
  </section>

  <section class="card card-back" aria-label="Business card back">
    <div class="back-brand">
      <span class="brand-circle"></span>
      <div class="brand-name">
        <span class="firm">Dunstan &amp; Co</span>
        <span class="practice">Lawyers &amp; Migration Agents</span>
      </div>
    </div>
    <div class="back-web">www.permitpath-example.org.au</div>
  </section>

</body>
</html>
```